Need Pagesmith website design for tutoring service startup

We are a tutoring service out of Tucson, Arizona, called 'Harbor Study LLC,' and we are looking for a website that communicates academic success but doesn't take itself too seriously. The website should have artistic themes inspired by the Sonoran desert (or nature in general) and the great horned owl. Our main goal is to help students get the grades they want. We want to be a trusted provider of academic help to those who need it.
We provide all subject tutoring (including exam prep), mainly for high school and undergraduate college students. The client would only pay for the time they spend with their tutor - no tutoring packages. The tutors can set their prices. Both online and In-person tutoring is available. I want this website to be compatible with the tutoring software we're using, lessonquill (lessonquill.example).
Pages we need - Home, Subjects, Our Team and Tutors, FAQs, Be a Tutor, Contact.
I want a Testimonials section somewhere on the home page.
Websites I like:
coachmyclassmates.example
tinplum.example
mentorlens.example
My competitors:
mathsummitcoaching.example
dravicprivatecoaching.example
This is my first time using artflockly, so I hope this is a good brief. Let me know if you need more details.
Highschool students, college students, and the parents of those students

```html
<!DOCTYPE html>
<html lang="en">
<head>
<meta charset="utf-8">
<title>Harbor Study LLC – Home</title>
<link rel="stylesheet" href="https://fonts.googleapis.com/css2?family=IBM+Plex+Sans:wght@400;500;600&family=Roboto:wght@300;400;500&display=swap">
<style>
:root{
  --ink:#2c1b14;
  --bark:#875c3d;
  --ember:#b86a34;
  --cream:#f6f2f0;
  --white:#ffffff;
  --board:#e6e2e0;
  --muted:#8a7f7a;
  --line:#d9d1cc;
  --sand:#e8e0da;
}
*{margin:0;padding:0;box-sizing:border-box}
html,body{width:1200px;height:3911px;overflow:hidden}
body{background:var(--board);font-family:'Roboto',sans-serif;color:var(--ink);position:relative}
.abs{position:absolute}
.head{font-family:'IBM Plex Sans',sans-serif}
.accent{color:var(--bark)}

/* board header */
.brand{display:flex;align-items:center;gap:10px;font-family:'IBM Plex Sans',sans-serif;font-weight:500;color:var(--ink)}
.brand-dot{width:14px;height:14px;border-radius:50%;background:var(--ember);flex:none}
.board-divider{width:1px;height:92px;background:#cfc8c4}
.board-label{font-family:'IBM Plex Sans',sans-serif;font-size:25px;color:var(--ink)}
.board-font{font-family:'Roboto',sans-serif;font-size:15px;color:#4a3a33}
.swatch{width:40px;height:40px;border-radius:50%}
.swatch-code{font-size:10px;color:#6b5f5a;width:60px;text-align:center}

/* site */
.site{position:absolute;left:222px;top:289px;width:790px;height:3524px;overflow:hidden;background:var(--cream)}
.band{position:absolute;left:0;width:790px}
.wave{position:absolute;left:0;display:block}

.nav-link{font-size:8.5px;color:var(--ink);top:29px}
.btn{position:absolute;display:flex;align-items:center;justify-content:center;font-size:7.5px;font-weight:500;border-radius:2px}
.btn-solid{background:var(--ember);color:#fff}
.btn-outline{border:1px solid var(--ember);color:var(--ember);background:transparent}

.eyebrow{font-size:7px;letter-spacing:2px;color:var(--muted)}
.h1{font-family:'IBM Plex Sans',sans-serif;font-size:27px;font-weight:500;line-height:35px;color:var(--ink)}
.h2{font-family:'IBM Plex Sans',sans-serif;font-size:22px;font-weight:500;color:var(--ink);line-height:28px}
.body-sm{font-size:8px;line-height:15px;color:#6b5f5a}
.placeholder{border-radius:2px}

.step{position:absolute;left:98px;width:134px;height:40px;border:1.5px solid #cfc6c0;border-radius:4px;background:var(--white);font-size:8px;display:flex;align-items:center;padding-left:13px;color:var(--ink)}
.step.active{background:var(--ink);border-color:var(--ink);color:#fff}

.subject-card{position:absolute;width:183px;height:49px;background:var(--white);border-radius:3px;display:flex;align-items:center;padding-left:8px;gap:10px}
.subject-icon{width:34px;height:34px;background:var(--cream);border-radius:3px;display:flex;align-items:center;justify-content:center}
.subject-name{font-size:9px;color:var(--ink)}
.subject-meta{font-size:6px;color:var(--muted);margin-top:3px}

.tutor-card{position:absolute;top:2142px;width:183px;height:245px;background:var(--white);box-shadow:0 2px 8px rgba(44,27,20,.06)}
.tutor-photo{position:absolute;left:9px;top:10px;width:165px;height:181px}
.tutor-name{position:absolute;left:0;width:100%;top:209px;text-align:center;font-size:10px;font-weight:500}
.tutor-role{position:absolute;left:0;width:100%;top:225px;text-align:center;font-size:6.5px;color:var(--muted)}

.faq{position:absolute;width:258px;font-size:8.5px;font-weight:500;color:var(--ink);padding-bottom:8px;border-bottom:1px solid var(--line);display:flex;justify-content:space-between}
.faq span:last-child{color:var(--ember)}

.foot-head{font-size:10px;font-weight:500;color:#fff}
.foot-link{font-size:7px;color:#b9aaa2;line-height:15px}
.social{position:absolute;top:3418px;width:24px;height:24px;border-radius:50%;border:1px solid #6a5850}
</style>
</head>
<body>

<!-- board header -->
<div class="abs brand" style="left:207px;top:118px;font-size:26px;line-height:26px">
  <span class="brand-dot"></span><span style="width:140px">Harbor Study LLC</span>
</div>
<div class="abs board-divider" style="left:442px;top:109px"></div>
<div class="abs board-divider" style="left:735px;top:109px"></div>
<div class="abs board-label" style="left:538px;top:104px">Fonts:</div>
<div class="abs board-font" style="left:538px;top:153px">IBM Plex Sans</div>
<div class="abs board-font" style="left:538px;top:179px">Roboto</div>
<div class="abs board-label" style="left:829px;top:104px">Colors:</div>
<div class="abs swatch" style="left:814px;top:141px;background:var(--ink)"></div>
<div class="abs swatch" style="left:886px;top:141px;background:var(--bark)"></div>
<div class="abs swatch" style="left:940px;top:141px;background:var(--ember)"></div>
<div class="abs swatch" style="left:992px;top:141px;background:var(--cream)"></div>
<div class="abs swatch-code" style="left:804px;top:190px">#2c1b14</div>
<div class="abs swatch-code" style="left:876px;top:190px">#875c3d</div>
<div class="abs swatch-code" style="left:930px;top:190px">#b86a34</div>
<div class="abs swatch-code" style="left:982px;top:190px">#f6f2f0</div>

<!-- website -->
<main class="site">
  <!-- section backgrounds -->
  <div class="band" style="top:0;height:470px;background:var(--cream)"></div>
  <div class="band" style="top:460px;height:340px;background:var(--white)"></div>
  <div class="band" style="top:826px;height:380px;background:var(--cream)"></div>
  <div class="band" style="top:1206px;height:446px;background:var(--ink)"></div>
  <div class="band" style="top:1652px;height:420px;background:var(--cream)"></div>
  <div class="band" style="top:2072px;height:410px;background:var(--white)"></div>
  <div class="band" style="top:2496px;height:401px;background:var(--cream)"></div>
  <div class="band" style="top:2897px;height:339px;background:var(--white)"></div>
  <div class="band" style="top:3236px;height:288px;background:var(--ink)"></div>

  <!-- waves -->
  <svg class="wave" style="top:410px" width="790" height="64" viewBox="0 0 790 64" preserveAspectRatio="none"><path d="M0,50 C140,34 300,8 470,14 C600,18 700,52 790,40 L790,64 L0,64Z" fill="#ffffff"/></svg>
  <svg class="wave" style="top:762px" width="790" height="66" viewBox="0 0 790 66" preserveAspectRatio="none"><path d="M0,20 C140,44 300,56 470,48 C620,40 720,20 790,0 L790,66 L0,66Z" fill="#f6f2f0"/></svg>
  <svg class="wave" style="top:2010px" width="790" height="64" viewBox="0 0 790 64" preserveAspectRatio="none"><path d="M0,34 C150,10 300,4 440,22 C580,40 700,32 790,14 L790,64 L0,64Z" fill="#ffffff"/></svg>
  <svg class="wave" style="top:2436px" width="790" height="62" viewBox="0 0 790 62" preserveAspectRatio="none"><path d="M0,6 C140,30 300,44 470,40 C620,36 720,22 790,0 L790,62 L0,62Z" fill="#f6f2f0"/></svg>

  <!-- nav -->
  <div class="abs brand" style="left:106px;top:24px;font-size:11px;line-height:11px">
    <span class="brand-dot" style="width:9px;height:9px"></span><span style="width:62px">Harbor Study LLC</span>
  </div>
  <div class="abs nav-link" style="left:238px">Home</div>
  <div class="abs nav-link" style="left:289px">Subjects</div>
  <div class="abs nav-link" style="left:350px">Our Team &amp; Tutors</div>
  <div class="abs nav-link" style="left:449px">FAQs</div>
  <div class="abs nav-link" style="left:495px">Become a Tutor</div>
  <div class="btn btn-outline" style="left:614px;top:21px;width:71px;height:25px;font-weight:400">Contact Us</div>
  <div class="abs" style="left:0;top:64px;width:790px;height:1px;background:var(--line)"></div>

  <!-- hero -->
  <div class="abs eyebrow" style="left:106px;top:125px">HIGHER SCORES · AFFORDABLE TUTORING</div>
  <h1 class="abs h1" style="left:106px;top:140px;width:320px">Get Better Results with <span class="accent">our Result-Oriented</span> Tutoring &amp; Exam Prep.</h1>
  <div class="abs" style="left:106px;top:262px;width:2px;height:27px;background:var(--ink)"></div>
  <p class="abs body-sm" style="left:118px;top:259px;width:260px">We provide all subject tutoring (including exam prep), mainly for high school and undergraduate college students.</p>
  <div class="btn btn-solid" style="left:106px;top:310px;width:76px;height:26px">I'm Interested</div>
  <svg class="abs" style="left:196px;top:304px" width="16" height="28" viewBox="0 0 16 28"><path d="M3,4 C12,2 13,10 6,12 C14,13 13,22 4,22 M4,22 l4,-3 M4,22 l3,4" fill="none" stroke="var(--ink)" stroke-width="1.2" stroke-linecap="round"/></svg>

  <div class="abs" style="left:440px;top:198px;width:271px;height:271px;border-radius:50%;border:1.5px solid var(--sand)"></div>
  <div class="abs" style="left:462px;top:220px;width:228px;height:228px;border-radius:50%;background:var(--sand)"></div>
  <div class="abs placeholder" role="img" aria-label="Photo of a smiling tutor in a dark blazer holding a laptop" style="left:472px;top:100px;width:212px;height:370px;border-radius:100px 100px 0 0;background:linear-gradient(180deg,#6b4a3a 0%,#3a2a24 45%,#2a2220 100%)"></div>
  <div class="abs" style="left:633px;top:202px;width:50px;height:48px;background:var(--ember);border-radius:3px;display:flex;align-items:center;justify-content:center">
    <svg width="20" height="18" viewBox="0 0 20 18"><path d="M2,16 H18 M4,14 V10 M8,14 V8 M12,14 V6 M16,14 V4 M3,9 L8,5 L12,6 L17,2" fill="none" stroke="#fff" stroke-width="1.3"/></svg>
  </div>
  <div class="abs" style="left:428px;top:261px;width:45px;height:46px;background:var(--white);border-radius:3px;display:flex;align-items:center;justify-content:center;box-shadow:0 2px 6px rgba(44,27,20,.08)">
    <svg width="22" height="20" viewBox="0 0 22 20"><rect x="3" y="2" width="16" height="11" fill="none" stroke="var(--ink)" stroke-width="1.1"/><path d="M1,16 H21 M7,13 V16 M15,13 V16 M8,6 H14 M8,9 H12" stroke="var(--ink)" stroke-width="1.1"/></svg>
  </div>

  <!-- how it works -->
  <h2 class="abs h2" style="left:100px;top:504px">How It <span class="accent">Works</span></h2>
  <div class="step" style="top:557px">1. Tell Us What You Need</div>
  <div class="step active" style="top:607px">2. Find Your Tutor</div>
  <div class="step" style="top:657px">3. Meet Online or In Person</div>
  <div class="step" style="top:708px">4. Get Desired Results</div>
  <div class="abs placeholder" role="img" aria-label="Photo of a student writing notes at a desk" style="left:258px;top:557px;width:254px;height:191px;background:linear-gradient(135deg,#7a5a45 0%,#c9b3a2 55%,#eee6df 100%)"></div>
  <p class="abs body-sm" style="left:538px;top:555px;width:145px">Lorem ipsum dolor sit amet, setur dated adipiscing elit, sed do eiumod tempor incididunt ut labore et dolore magna aliqua. Quis ipsum mos at suspendisse ultrices raeptal.</p>
  <p class="abs body-sm" style="left:538px;top:646px;width:145px">Lorem ipsum dolor sit amet, setur dated adipiscing elit, sed do eiumod tempor incididunt ut labore et dolore magna aliqua. Quis ipsum mos suspendisse ultrices raeptal.</p>

  <!-- subjects -->
  <h2 class="abs h2" style="left:0;width:790px;text-align:center;top:880px">Main <span class="accent">Subjects</span> to Learn</h2>
  <p class="abs" style="left:0;width:790px;text-align:center;top:925px;font-size:7px;color:var(--muted)">Our 1-on-1 private tutoring service is built to serve each student differently</p>

  <div class="subject-card" style="left:106px;top:962px"><div class="subject-icon"><svg width="18" height="18" viewBox="0 0 18 18"><rect x="1" y="1" width="16" height="16" fill="none" stroke="var(--ink)"/><path d="M9,1 V17 M1,9 H17 M3,5 H7 M5,3 V7 M11,5 H15 M3,13 H7 M11,12 H15 M11,14 H15" stroke="var(--ink)"/></svg></div><div><div class="subject-name">Mathematics</div><div class="subject-meta">17 Tutoring Courses</div></div></div>
  <div class="subject-card" style="left:303px;top:962px"><div class="subject-icon"><svg width="18" height="18" viewBox="0 0 18 18"><ellipse cx="9" cy="9" rx="8" ry="3" fill="none" stroke="var(--ink)"/><ellipse cx="9" cy="9" rx="8" ry="3" transform="rotate(60 9 9)" fill="none" stroke="var(--ink)"/><ellipse cx="9" cy="9" rx="8" ry="3" transform="rotate(-60 9 9)" fill="none" stroke="var(--ink)"/><circle cx="9" cy="9" r="1.3" fill="var(--ink)"/></svg></div><div><div class="subject-name">Science</div><div class="subject-meta">17 Tutoring Courses</div></div></div>
  <div class="subject-card" style="left:501px;top:962px"><div class="subject-icon"><svg width="18" height="18" viewBox="0 0 18 18"><path d="M2,2 H16 M5,2 V8 M13,2 V8 M9,2 V12" stroke="var(--ink)"/><circle cx="5" cy="10" r="2" fill="none" stroke="var(--ink)"/><circle cx="13" cy="10" r="2" fill="none" stroke="var(--ink)"/><circle cx="9" cy="14" r="2" fill="none" stroke="var(--ink)"/></svg></div><div><div class="subject-name">Physics</div><div class="subject-meta">17 Tutoring Courses</div></div></div>
  <div class="subject-card" style="left:106px;top:1026px"><div class="subject-icon"><svg width="18" height="18" viewBox="0 0 18 18"><path d="M6,1 H12 M7,1 V7 L2,16 H16 L11,7 V1 M4,12 H14" fill="none" stroke="var(--ink)"/></svg></div><div><div class="subject-name">Chemistry</div><div class="subject-meta">17 Tutoring Courses</div></div></div>
  <div class="subject-card" style="left:303px;top:1026px"><div class="subject-icon"><svg width="18" height="18" viewBox="0 0 18 18"><path d="M5,1 C13,5 5,13 13,17 M13,1 C5,5 13,13 5,17 M6,4 H12 M6,9 H12 M6,14 H12" fill="none" stroke="var(--ink)"/></svg></div><div><div class="subject-name">Biology</div><div class="subject-meta">17 Tutoring Courses</div></div></div>
  <div class="subject-card" style="left:501px;top:1026px"><div class="subject-icon"><svg width="18" height="18" viewBox="0 0 18 18"><path d="M3,9 L14,3 L16,7 L5,13Z M9,10 L6,17 M9,10 L12,17" fill="none" stroke="var(--ink)"/></svg></div><div><div class="subject-name">Astronomy</div><div class="subject-meta">17 Tutoring Courses</div></div></div>

  <p class="abs" style="left:0;width:790px;text-align:center;top:1111px;font-size:7px;color:var(--ink)">You Don't See the Subject You Need Help With? <span style="color:var(--ember);text-decoration:underline">Click Here to View All Subjects</span></p>

  <!-- learning preferences -->
  <div class="abs" style="left:97px;top:1365px;width:60px;height:77px;background:#3d2a21"></div>
  <div class="abs placeholder" role="img" aria-label="Photo of a group of students studying together around a laptop" style="left:106px;top:1181px;width:579px;height:252px;background:linear-gradient(120deg,#c9a98a 0%,#8a6a52 40%,#5a4438 70%,#b7a08c 100%)"></div>
  <div class="abs" style="left:530px;top:1335px;width:175px;height:75px;background:var(--cream);border-radius:3px;display:flex;align-items:center;padding-left:18px;gap:8px">
    <div style="display:flex">
      <span role="img" aria-label="Student avatar" style="width:20px;height:20px;border-radius:50%;background:#9a7a66;border:2px solid #fff"></span>
      <span role="img" aria-label="Student avatar" style="width:20px;height:20px;border-radius:50%;background:#b8917a;border:2px solid #fff;margin-left:-6px"></span>
      <span role="img" aria-label="Student avatar" style="width:20px;height:20px;border-radius:50%;background:#6f5344;border:2px solid #fff;margin-left:-6px"></span>
      <span role="img" aria-label="Student avatar" style="width:20px;height:20px;border-radius:50%;background:#c7a996;border:2px solid #fff;margin-left:-6px"></span>
    </div>
    <div style="font-size:8px;font-weight:500;line-height:10px">+500 Students<br>Registered</div>
  </div>
  <h2 class="abs head" style="left:0;width:790px;text-align:center;top:1470px;font-size:21px;font-weight:500;color:#fff">Students Have Their Own Learning Preferences. Get Yours.</h2>
  <p class="abs" style="left:200px;width:390px;text-align:center;top:1514px;font-size:8px;line-height:16px;color:#d8ccc5">Lorem ipsum dolor sit amet, consectetur adipiscing elit, sed do eiusmod tempor incididunt ut labore et dolore magna aliqua. Quis ipsum suspendisse ultrices gravida. Risus commodo viverra.</p>
  <div class="btn btn-solid" style="left:361px;top:1566px;width:70px;height:25px">Talk to a Tutor</div>

  <!-- experts -->
  <div class="abs" style="left:125px;top:1773px;width:181px;height:167px;background:var(--sand)"></div>
  <div class="abs" style="left:163px;top:1709px;width:182px;height:172px;background:var(--white);box-shadow:0 2px 10px rgba(44,27,20,.06)"></div>
  <div class="abs" role="img" aria-label="Tutor portrait" style="left:234px;top:1760px;width:40px;height:40px;border-radius:50%;background:#8d7a70;border:2px solid var(--sand)"></div>
  <div class="abs" style="left:163px;width:182px;text-align:center;top:1808px;font-size:9px;font-weight:500">Corin Valdes</div>
  <div class="abs" style="left:163px;width:182px;text-align:center;top:1823px;font-size:6px;color:var(--muted)">17 Exams for Students</div>
  <div class="abs" style="left:106px;top:1900px;width:174px;height:76px;background:var(--white);box-shadow:0 2px 10px rgba(44,27,20,.08);display:flex;align-items:center;padding-left:28px;gap:8px">
    <span role="img" aria-label="Tutor portrait" style="width:40px;height:40px;border-radius:50%;background:#b89a88;flex:none"></span>
    <div><div style="font-size:9px;font-weight:500">Nadia Forde</div><div style="font-size:6px;color:var(--muted);margin-top:3px">17 Exams for Students</div></div>
  </div>
  <h2 class="abs h2" style="left:464px;top:1729px;width:240px;font-size:21px;line-height:27px">Learn from Approved <span class="accent">Experts</span> at Your Own Space and Comfort</h2>
  <p class="abs" style="left:464px;top:1831px;font-size:8px;color:#6b5f5a">9/10 users reported better learning outcomes.</p>
  <p class="abs body-sm" style="left:464px;top:1855px;width:230px">Lorem ipsum dolor sit amet, consectetur adipiscing elit, sed do eiusmod tempor incididunt ut labore et dolore magna aliqua. Quis ipsum suspendisse ultrices gravida.</p>
  <div class="btn btn-outline" style="left:464px;top:1926px;width:70px;height:25px">Enroll Today</div>

  <!-- team -->
  <h2 class="abs h2" style="left:106px;top:2230px;font-size:22px">Meet Our<br><span class="accent">Team &amp; Tutors</span></h2>
  <div class="tutor-card" style="left:303px"><div class="tutor-photo" role="img" aria-label="Portrait of a smiling male tutor in a light sweater" style="background:linear-gradient(180deg,#e9e4e0,#c9bdb4)"></div><div class="tutor-name">Elias Morrow</div><div class="tutor-role">Math Tutor</div></div>
  <div class="tutor-card" style="left:501px"><div class="tutor-photo" role="img" aria-label="Portrait of a female tutor in a dark blazer holding a folder" style="background:linear-gradient(180deg,#e9e4e0,#3d3330)"></div><div class="tutor-name">Dana Morrow</div><div class="tutor-role">Biology Tutor</div></div>
  <div class="tutor-card" style="left:698px"><div class="tutor-photo" role="img" aria-label="Portrait of a male tutor in a suit" style="background:linear-gradient(180deg,#e9e4e0,#2f2825)"></div><div class="tutor-name">Elias Morrow</div><div class="tutor-role">Math Tutor</div></div>
  <div class="abs" style="left:582px;top:2407px;width:4px;height:4px;border-radius:50%;background:#e3b79a"></div>
  <div class="abs" style="left:592px;top:2407px;width:4px;height:4px;border-radius:50%;background:var(--ember)"></div>
  <div class="abs" style="left:602px;top:2407px;width:4px;height:4px;border-radius:50%;background:#e3b79a"></div>

  <!-- testimonial -->
  <div class="abs" style="left:128px;top:2561px;width:236px;height:264px;background:var(--sand)"></div>
  <div class="abs placeholder" role="img" aria-label="Photo of a smiling college student with glasses and a backpack" style="left:106px;top:2572px;width:247px;height:266px;background:linear-gradient(160deg,#b9b2aa 0%,#8c8078 50%,#d8d0c8 100%)"></div>
  <svg class="abs" style="left:431px;top:2698px" width="8" height="12" viewBox="0 0 8 12"><path d="M6,1 L2,6 L6,11" fill="none" stroke="var(--ember)" stroke-width="1.3"/></svg>
  <svg class="abs" style="left:678px;top:2698px" width="8" height="12" viewBox="0 0 8 12"><path d="M2,1 L6,6 L2,11" fill="none" stroke="var(--ember)" stroke-width="1.3"/></svg>
  <div class="abs head" style="left:448px;top:2636px;font-size:34px;font-weight:600;line-height:34px;color:var(--ink)">&rdquo;</div>
  <p class="abs" style="left:448px;top:2677px;width:220px;font-size:8px;line-height:15.5px;font-style:italic;color:#6b5f5a">Lorem ipsum dolor sit amet, consectetur adipiscing elit, sed do eiusmod tempor incididunt ut labore et dolore magna aliqua. Quis ipsum suspendisse ultrices gravida.</p>
  <div class="abs" style="left:448px;top:2737px;font-size:8.5px;color:var(--ink)">Marcus Hale</div>
  <div class="abs" style="left:448px;top:2752px;font-size:6px;color:var(--muted)">Undergraduate College Student</div>

  <!-- faq -->
  <h2 class="abs h2" style="left:0;width:790px;text-align:center;top:2952px">Frequently <span class="accent">Asked</span> Questions</h2>
  <p class="abs" style="left:0;width:790px;text-align:center;top:2999px;font-size:7px;color:var(--muted)">Our 1-on-1 private tutoring service is built to serve each student differently</p>
  <div class="faq" style="left:126px;top:3036px"><span>How does online tuition differ from tuition in person?</span><span>+</span></div>
  <div class="faq" style="left:407px;top:3036px"><span>What Is Expected From Me During Sessions?</span><span>+</span></div>
  <div class="faq" style="left:126px;top:3075px"><span>How Can I Schedule a Session With a Tutor?</span><span>+</span></div>
  <div class="faq" style="left:407px;top:3075px"><span>Will My Tutor Just Give Me the Answers?</span><span>+</span></div>
  <div class="faq" style="left:126px;top:3115px"><span>What Happens if a Tutor Cancels a Session?</span><span>+</span></div>
  <div class="faq" style="left:407px;top:3115px"><span>What If the Subject I Want is Not Listed?</span><span>+</span></div>
  <div class="faq" style="left:126px;top:3154px"><span>How Do I Become a Tutor?</span><span>+</span></div>
  <div class="faq" style="left:407px;top:3154px"><span>How Do You Ensure Quality and Satisfied Results?</span><span>+</span></div>

  <!-- footer -->
  <div class="abs brand" style="left:106px;top:3304px;font-size:11px;line-height:11px;color:#fff">
    <span class="brand-dot" style="width:9px;height:9px"></span><span style="width:62px">Harbor Study LLC</span>
  </div>
  <div class="abs" style="left:106px;top:3344px;font-size:6px;color:var(--ember)">© 2023 - Harbor Study</div>

  <div class="abs" style="left:292px;top:3296px"><div class="foot-head">Top Subjects</div><div style="margin-top:8px"><div class="foot-link">Algebra Tutor Online</div><div class="foot-link">Chemistry Tutor Online</div><div class="foot-link">Biology Tutor Online</div></div></div>
  <div class="abs" style="left:476px;top:3296px"><div class="foot-head">Helpful Links</div><div style="margin-top:8px"><div class="foot-link">Exam Prep</div><div class="foot-link">Our Team &amp; Tutors</div><div class="foot-link">Become a Tutor</div></div></div>
  <div class="abs" style="left:646px;top:3296px"><div class="foot-head">Support</div><div style="margin-top:8px"><div class="foot-link">About Us</div><div class="foot-link">FAQs</div></div></div>

  <div class="abs foot-head" style="left:287px;top:3393px">Find Us Here</div>
  <div class="social" style="left:289px"></div>
  <div class="social" style="left:322px"></div>
  <div class="social" style="left:354px"></div>
  <div class="btn btn-solid" style="left:476px;top:3419px;width:89px;height:24px">Start Your Journey</div>
</main>

</body>
</html>
```